Introduction:
We are an Australia-based Cyber Security Penetration testing company seeking a website redesign to showcase our services, expertise, and experience. Our target audience includes businesses and organizations of all sizes who are seeking to secure their IT infrastructure against cyber threats. The purpose of the website redesign is to increase our online presence, generate leads, and establish our company as a trusted authority in the industry.
Objectives:
Create a professional and modern website that is easy to navigate and user-friendly.
Provide information about our company, services, and expertise.
Clearly display table of our 3 services: Bug Bounty as a Service, Penetration Testing and Code Review.
Generate leads through online contact forms and calls-to-action.
Optimize the website for search engines to increase visibility and traffic.
Website similar to: https://www.velmora.com.au/.
Target Audience:
Our target audience includes businesses and organizations of all sizes that require cybersecurity penetration testing services. These include:
Small and medium-sized enterprises (SMEs)
Australian Government agencies
Design Requirements:
Clean, modern, and professional design.
Use of colors that convey trust, reliability, and expertise (such as orange and grey).
Calls-to-action that encourage visitors to contact us or request a quote.
Integration with social media channels to increase engagement and brand awareness.
A blog section to showcase our thought leadership and expertise.
A news section to share updates about our company and the industry.
Content Requirements:
Home page that introduces our company and services and highlights our expertise.
About Us page that provides information about our company, team, and values.
Services page that lists our services and explains the benefits of each.
Case Studies page that showcases our previous work and success stories.
Contact Us page that includes a contact form, phone number, and email address.
Blog section with articles related to the cybersecurity industry and our services.
News section with updates about our company and the industry.

```html
<!DOCTYPE html>
<html lang="en">
<head>
<meta charset="utf-8">
<title>Emberstrat – Website Page Designs</title>
<link href="https://fonts.googleapis.com/css2?family=Montserrat:wght@400;500;600;700&display=swap" rel="stylesheet">
<style>
:root{
  --bg:#e8e9eb;
  --orange:#ec6a3d;
  --amber:#f0962f;
  --gold:#f2a941;
  --peach:#f6c990;
  --cream:#fbe5cf;
  --shell:#fdf3ea;
  --grey:#555557;
  --dark:#3f3f41;
  --ink:#2b2b2b;
  --soft:#ececec;
  --white:#ffffff;
}
*{margin:0;padding:0;box-sizing:border-box}
html,body{width:1200px;height:637px;overflow:hidden;background:var(--bg);font-family:'Montserrat',sans-serif;color:var(--ink)}
.board{position:relative;width:1200px;height:637px}
.page{position:absolute;top:153px;width:171px;height:361px;background:var(--white);overflow:hidden;box-shadow:0 1px 3px rgba(0,0,0,.12)}
.page > *{position:absolute;left:0;width:100%}

/* top bar */
.topbar{top:0;height:6.5px;background:var(--grey);display:flex;align-items:center;padding:0 5px;gap:2px}
.topbar .socials{display:flex;gap:1.3px}
.topbar .socials i{width:2.4px;height:2.4px;border-radius:50%;background:var(--white);display:block}
.topbar .tel{margin-left:auto;font-size:1.4px;color:var(--white)}
.topbar .call{font-size:1.2px;color:var(--white);background:var(--orange);padding:.6px 2px;font-weight:700}

/* header */
.site-header{top:6.5px;height:11px;background:var(--white)}
.brand{position:absolute;left:6px;top:1.5px;display:flex;flex-direction:column;align-items:flex-start;gap:.4px}
.brand-mark{width:4px;height:4px;border-radius:50%;border:.6px solid var(--orange)}
.brand-name{font-size:2.2px;font-weight:700;color:var(--orange)}
.nav{position:absolute;left:56px;right:3px;top:4.5px;display:flex;justify-content:space-between}
.nav span{font-size:1.7px;color:var(--ink);position:relative}
.nav span.on{font-weight:700}
.nav span.on::after{content:"";position:absolute;left:-1px;right:-1px;top:4.6px;height:.8px;background:var(--orange)}

/* shared type */
.page-title{text-align:center;font-size:7.4px;font-weight:600;letter-spacing:.1px;color:var(--ink)}
.page-title em{font-style:normal;color:var(--orange)}
.copy{font-size:1.9px;line-height:2.45px;text-align:center;color:var(--ink);padding:0 14px}
.copy p+p{margin-top:1.6px}
.copy.light{color:var(--white)}

/* footer */
.site-footer{top:313px;height:48px;background:var(--grey);color:var(--white)}
.site-footer .brand{left:13px;top:9px}
.foot-about{position:absolute;left:13px;top:20px;width:32px;font-size:1.5px;line-height:1.9px}
.foot-col{position:absolute;top:8px;font-size:1.4px;line-height:3.2px}
.foot-col h4{font-size:1.9px;font-weight:700;margin-bottom:1.3px}
.foot-col.c1{left:57px}.foot-col.c2{left:92px}.foot-col.c3{left:130px}
.foot-col .dots{display:flex;gap:1.3px;margin-top:1px}
.foot-col .dots i{width:2.6px;height:2.6px;border-radius:50%;background:var(--white);display:block}
.copyright{position:absolute;left:13px;top:41px;font-size:1.3px}

/* photo placeholders */
.photo-city{background:linear-gradient(160deg,#5c6b80 0%,#2d3442 45%,#a06a3a 75%,#1f2430 100%)}
.photo-tech{background:radial-gradient(ellipse at 40% 60%,#2d7fb8 0%,#163556 40%,#0c1727 100%)}

/* home */
.hero{top:17.5px;height:72px}
.hero-band{position:absolute;left:0;right:0;top:21px;height:7px;background:var(--orange)}
.hero-title{position:absolute;left:0;right:0;top:20.6px;text-align:center;font-size:7.4px;line-height:8px;font-weight:600;color:var(--white)}
.hero-copy{position:absolute;left:50px;right:50px;top:31px;font-size:1.8px;line-height:2.3px;text-align:center;color:var(--white)}
.btn{display:inline-block;background:var(--orange);color:var(--white);font-weight:600}
.hero .btn{position:absolute;left:73px;top:46px;width:25px;height:4px;font-size:1.5px;line-height:4px;text-align:center}
.hero-dots{position:absolute;left:80px;top:61px;display:flex;gap:1px}
.hero-dots i{width:2px;height:2px;border-radius:50%;background:rgba(255,255,255,.5);display:block}
.hero-dots i:first-child{background:var(--white)}
.skills{top:89.5px;height:68px}
.skills .page-title{position:absolute;left:0;right:0;top:6px;font-size:5.6px;line-height:6px}
.skills .copy{position:absolute;left:40px;right:40px;top:14px;padding:0}
.skill{position:absolute;top:23px;width:26px;height:32px}
.skill svg{position:absolute;left:0;top:0;width:26px;height:26px;display:block}
.skill small{position:absolute;left:0;right:0;top:27.5px;text-align:center;font-size:1.5px;line-height:1.8px;font-weight:700}
.why{top:157.5px;height:73px;background:var(--orange);color:var(--white)}
.why .page-title{position:absolute;left:0;right:0;top:6px;font-size:5.4px;line-height:6px;color:var(--white)}
.why .copy{position:absolute;left:40px;right:40px;top:13px;padding:0}
.feature{position:absolute;top:25px;width:30px;text-align:center}
.feature .ring{width:22px;height:22px;margin:0 auto;border-radius:50%;background:var(--white);display:flex;align-items:center;justify-content:center}
.feature h5{font-size:1.5px;line-height:1.8px;font-weight:700;margin-top:2.2px}
.feature p{font-size:1.3px;line-height:1.6px;margin-top:.5px}
.feature .go{width:3.6px;height:2.6px;margin:1px auto 0;background:var(--white)}
.gov{top:230px;height:83px}
.gov-text{position:absolute;right:16px;top:32px;text-align:right;color:var(--white)}
.gov-text small{font-size:1.8px;line-height:2.2px;display:block;margin-bottom:1px}
.gov-text strong{font-size:8.2px;line-height:9px;font-weight:700;display:block}

/* about */
.about-title{top:27px;line-height:8px}
.about-copy{top:42px}
.excellence{top:96px;height:105px;background:var(--orange)}
.excellence .page-title{position:absolute;left:0;right:0;top:13px;color:var(--white);font-size:7px;line-height:8px}
.excellence .copy{position:absolute;left:0;right:0;top:30px}
.value-dots{position:absolute;top:75px;left:0;right:0}
.value-dots i{position:absolute;width:21.5px;height:21.5px;border-radius:50%;background:var(--white);display:block}
.about-photo{top:201px;height:112px}

/* services */
.svc{position:absolute;width:36px;text-align:center}
.svc .ring{width:21px;height:21px;margin:0 auto;border-radius:50%;background:var(--soft);display:flex;align-items:center;justify-content:center}
.svc h5{font-size:1.5px;line-height:1.8px;font-weight:700;margin-top:2.5px}
.svc p{font-size:1.2px;line-height:1.5px;color:#777;margin-top:.4px}
.svc .go{width:4px;height:2.8px;margin:1px auto 0;background:var(--orange)}
.svc-copy1{top:94px}
.svc-copy2{top:250px}

/* case studies */
.case-block{top:46px;height:86px;background:var(--orange)}
.case-grid{position:absolute;left:10.5px;top:14px;width:148px;height:60px;display:grid;grid-template-columns:repeat(5,1fr);grid-template-rows:repeat(2,1fr)}
.case-grid div{display:flex;align-items:center;justify-content:center}
.case-grid svg{width:13px;height:13px}
.case-copy{top:140px}
.stats{top:283px;height:30px;background:var(--orange);color:var(--white)}
.stat{position:absolute;top:7px;width:34px;text-align:center}
.stat b{font-size:10px;font-weight:600;display:block;line-height:11px}
.stat small{font-size:1.6px;line-height:2px;font-weight:700;display:block}

/* blog */
.blog-card{position:absolute;width:74px;height:63px;padding:0 6px}
.blog-card h5{position:absolute;left:6px;top:41px;font-size:2.4px;line-height:2.8px;font-weight:700}
.blog-card p{position:absolute;left:6px;right:6px;top:45px;font-size:1.6px;line-height:2px}
.blog-card time{position:absolute;left:6px;top:51.5px;font-size:1.5px;line-height:1.8px;font-weight:700}
.blog-card.on-dark{color:var(--white)}
.blog-card.on-light{color:var(--ink)}

/* contact */
.contact-form{top:46px;height:118px;background:var(--cream)}
.field{position:absolute;left:14px;width:144px;background:var(--white);font-size:2.6px;line-height:3px;font-weight:600;padding:3.5px 3px}
.contact-form .btn{position:absolute;left:14px;top:103px;width:41px;height:10px;font-size:2.6px;line-height:10px;text-align:center}
.contact-lines{top:171px;font-size:2.2px;text-align:center;line-height:3px}
.contact-lines span{margin:0 4px}
.contact-lines svg{width:2.4px;height:2.4px;vertical-align:-.3px;margin-right:.8px}
.map{top:187px;height:47px;background:linear-gradient(180deg,#f4f4f4,#ececec)}
.follow{top:240px;text-align:center}
.follow h3{font-size:7px;line-height:8px;font-weight:600}
.follow h3 em{font-style:normal;color:var(--orange)}
.follow .dots{display:flex;justify-content:center;gap:2.5px;margin-top:3px}
.follow .dots i{width:10px;height:10px;border-radius:50%;background:var(--ink);display:block}
</style>
</head>
<body>
<div class="board">

<!-- HOME -->
<div class="page" style="left:40px">
  <div class="topbar"><div class="socials"><i></i><i></i><i></i><i></i><i></i></div><span class="tel">+61 2 5550 1140 &nbsp; +61 2 5550 1141</span><b class="call">CALL NOW</b></div>
  <header class="site-header"><div class="brand"><span class="brand-mark"></span><span class="brand-name">Emberstrat</span></div>
    <nav class="nav"><span class="on">HOME</span><span>ABOUT</span><span>SERVICES</span><span>CASE STUDIES</span><span>BLOG</span><span>NEWS</span><span>CONTACT US</span></nav></header>
  <section class="hero photo-tech" role="img" aria-label="Photo: hands on a laptop keyboard with a glowing digital security overlay">
    <div class="hero-band"></div>
    <h1 class="hero-title">WE ARE EXPERTS</h1>
    <p class="hero-copy">We find the weak points in your systems before attackers do, then help your team close every gap fast.</p>
    <span class="btn">READ MORE</span>
    <div class="hero-dots"><i></i><i></i><i></i></div>
  </section>
  <section class="skills">
    <h2 class="page-title">OUR <em>SKILLS</em></h2>
    <p class="copy">Skilled testers with deep hands-on knowledge across networks, apps and cloud.</p>
    <div class="skill" style="left:22px"><svg viewBox="0 0 26 26"><circle cx="13" cy="13" r="10" fill="none" stroke="#eee" stroke-width="2.4"/><circle cx="13" cy="13" r="10" fill="none" stroke="var(--orange)" stroke-width="2.4" stroke-dasharray="28.3 62.8" transform="rotate(-90 13 13)"/><text x="13" y="14.3" text-anchor="middle" font-size="3.6" font-weight="700" font-family="Montserrat,sans-serif">45%</text></svg><small>OUR SKILLS</small></div>
    <div class="skill" style="left:56px"><svg viewBox="0 0 26 26"><circle cx="13" cy="13" r="10" fill="none" stroke="#eee" stroke-width="2.4"/><circle cx="13" cy="13" r="10" fill="none" stroke="var(--amber)" stroke-width="2.4" stroke-dasharray="37.7 62.8" transform="rotate(-90 13 13)"/><text x="13" y="14.3" text-anchor="middle" font-size="3.6" font-weight="700" font-family="Montserrat,sans-serif">60%</text></svg><small>OUR SKILLS</small></div>
    <div class="skill" style="left:89px"><svg viewBox="0 0 26 26"><circle cx="13" cy="13" r="10" fill="none" stroke="#eee" stroke-width="2.4"/><circle cx="13" cy="13" r="10" fill="none" stroke="var(--peach)" stroke-width="2.4" stroke-dasharray="47.1 62.8" transform="rotate(-90 13 13)"/><text x="13" y="14.3" text-anchor="middle" font-size="3.6" font-weight="700" font-family="Montserrat,sans-serif">75%</text></svg><small>OUR SKILLS</small></div>
    <div class="skill" style="left:121px"><svg viewBox="0 0 26 26"><circle cx="13" cy="13" r="10" fill="none" stroke="#eee" stroke-width="2.4"/><circle cx="13" cy="13" r="10" fill="none" stroke="var(--dark)" stroke-width="2.4" stroke-dasharray="50.2 62.8" transform="rotate(-90 13 13)"/><text x="13" y="14.3" text-anchor="middle" font-size="3.6" font-weight="700" font-family="Montserrat,sans-serif">80%</text></svg><small>OUR SKILLS</small></div>
  </section>
  <section class="why">
    <h2 class="page-title">WHY CHOOSE US</h2>
    <p class="copy light">Certified experts, clear reports and fixes that stick, for teams of every size.</p>
    <div class="feature" style="left:32px"><div class="ring"><svg viewBox="0 0 20 20" width="13" height="13"><circle cx="8.5" cy="8.5" r="5.5" fill="none" stroke="#2b2b2b" stroke-width="1.2"/><line x1="12.5" y1="12.5" x2="17" y2="17" stroke="#2b2b2b" stroke-width="1.6"/><circle cx="8.5" cy="8.5" r="2" fill="none" stroke="#2b2b2b" stroke-width=".9"/></svg></div><h5>BUG BOUNTY</h5><p>Crowd testing run by our own expert team.</p><div class="go"></div></div>
    <div class="feature" style="left:69px"><div class="ring"><svg viewBox="0 0 20 20" width="13" height="13"><rect x="2.5" y="5" width="12" height="8" fill="none" stroke="#2b2b2b" stroke-width="1.1"/><line x1="1" y1="14.5" x2="16" y2="14.5" stroke="#2b2b2b" stroke-width="1.1"/><rect x="12" y="8" width="5" height="4" fill="#fff" stroke="#2b2b2b" stroke-width="1"/><path d="M13 8V6.5a1.5 1.5 0 013 0V8" fill="none" stroke="#2b2b2b" stroke-width="1"/></svg></div><h5>PENETRATION TESTING</h5><p>Real attack methods used to probe your setup.</p><div class="go"></div></div>
    <div class="feature" style="left:109px"><div class="ring"><svg viewBox="0 0 20 20" width="13" height="13"><circle cx="8.5" cy="8.5" r="5.5" fill="none" stroke="#2b2b2b" stroke-width="1.2"/><line x1="12.5" y1="12.5" x2="17" y2="17" stroke="#2b2b2b" stroke-width="1.6"/><path d="M7 6.5L5 8.5l2 2M10 6.5l2 2-2 2" fill="none" stroke="#2b2b2b" stroke-width=".9"/></svg></div><h5>CODE REVIEW</h5><p>Line by line checks of your source for flaws.</p><div class="go"></div></div>
  </section>
  <section class="gov photo-city" role="img" aria-label="Photo: harbour city skyline at dusk with an opera house">
    <div class="gov-text"><small>Emberstrat is Proudly</small><strong>AUSTRALIAN<br>GOVERNMENT<br>AGENCIES</strong></div>
  </section>
  <footer class="site-footer">
    <div class="brand"><span class="brand-mark" style="border-color:#fff"></span><span class="brand-name">Emberstrat</span></div>
    <p class="foot-about">Security testing for firms of all sizes, run by certified local experts who care.</p>
    <div class="foot-col c1"><h4>SERVICES</h4>Bug bounty<br>Pen testing<br>Code review<br>Cloud audit<br>Red team<br>Training<br>Advice</div>
    <div class="foot-col c2"><h4>USEFUL LINK</h4>About us<br>Case studies<br>Blog<br>News<br>Careers<br>Privacy<br>Terms</div>
    <div class="foot-col c3"><h4>CONTACTS</h4>(02) 5550 1140<br>(02) 5550 1141<br>hello@emberstrat.com.au<br><h4>FOLLOW US</h4><div class="dots"><i></i><i></i><i></i><i></i><i></i></div></div>
    <p class="copyright">copyright © 2023 Emberstrat</p>
  </footer>
</div>

<!-- ABOUT -->
<div class="page" style="left:230px">
  <div class="topbar"><div class="socials"><i></i><i></i><i></i><i></i><i></i></div><span class="tel">+61 2 5550 1140 &nbsp; +61 2 5550 1141</span><b class="call">CALL NOW</b></div>
  <header class="site-header"><div class="brand"><span class="brand-mark"></span><span class="brand-name">Emberstrat</span></div>
    <nav class="nav"><span>HOME</span><span class="on">ABOUT</span><span>SERVICES</span><span>CASE STUDIES</span><span>BLOG</span><span>NEWS</span><span>CONTACT US</span></nav></header>
  <h1 class="page-title about-title">ABOUT <em>US</em></h1>
  <div class="copy about-copy">
    <p>We are an Australian team of security testers who think like attackers. For years we have helped small firms, large groups and public bodies find and fix the gaps in their networks, apps and cloud platforms before anyone else can use them against them.</p>
    <p>Every test ends with a clear report, a risk rating for each issue and a plain plan your staff can act on today. We stay on hand to check the fixes and retest once they are done.</p>
  </div>
  <section class="excellence">
    <h2 class="page-title">EXCELLENCE AS STANDARD</h2>
    <div class="copy light">
      <p>Our people hold respected industry certificates and keep their skills sharp with ongoing research. We follow proven methods, keep your data safe through every step and respect the limits you set, so testing never gets in the way of your work.</p>
      <p>Clear scope, honest pricing and fast turnaround are part of every job we take on, big or small, from one web app to a full network.</p>
    </div>
    <div class="value-dots"><i style="left:19px"></i><i style="left:46px"></i><i style="left:73px"></i><i style="left:100px"></i><i style="left:127px"></i></div>
  </section>
  <section class="about-photo photo-tech" role="img" aria-label="Photo: person typing on a laptop with a glowing padlock overlay"></section>
  <footer class="site-footer">
    <div class="brand"><span class="brand-mark" style="border-color:#fff"></span><span class="brand-name">Emberstrat</span></div>
    <p class="foot-about">Security testing for firms of all sizes, run by certified local experts who care.</p>
    <div class="foot-col c1"><h4>SERVICES</h4>Bug bounty<br>Pen testing<br>Code review<br>Cloud audit<br>Red team<br>Training<br>Advice</div>
    <div class="foot-col c2"><h4>USEFUL LINK</h4>About us<br>Case studies<br>Blog<br>News<br>Careers<br>Privacy<br>Terms</div>
    <div class="foot-col c3"><h4>CONTACTS</h4>(02) 5550 1140<br>(02) 5550 1141<br>hello@emberstrat.com.au<br><h4>FOLLOW US</h4><div class="dots"><i></i><i></i><i></i><i></i><i></i></div></div>
    <p class="copyright">copyright © 2023 Emberstrat</p>
  </footer>
</div>

<!-- SERVICES -->
<div class="page" style="left:421px">
  <div class="topbar"><div class="socials"><i></i><i></i><i></i><i></i><i></i></div><span class="tel">+61 2 5550 1140 &nbsp; +61 2 5550 1141</span><b class="call">CALL NOW</b></div>
  <header class="site-header"><div class="brand"><span class="brand-mark"></span><span class="brand-name">Emberstrat</span></div>
    <nav class="nav"><span>HOME</span><span>ABOUT</span><span class="on">SERVICES</span><span>CASE STUDIES</span><span>BLOG</span><span>NEWS</span><span>CONTACT US</span></nav></header>
  <h1 class="page-title about-title">OUR <em>SERVICES</em></h1>

  <div class="svc" style="left:28px;top:43px"><div class="ring"><svg viewBox="0 0 20 20" width="13" height="13"><circle cx="8.5" cy="8.5" r="5.5" fill="none" stroke="#2b2b2b" stroke-width="1.2"/><line x1="12.5" y1="12.5" x2="17" y2="17" stroke="#2b2b2b" stroke-width="1.6"/><circle cx="8.5" cy="8.5" r="2" fill="none" stroke="#2b2b2b" stroke-width=".9"/></svg></div><h5>BUG BOUNTY</h5><p>Crowd testing run by our own expert team.</p><div class="go"></div></div>
  <div class="svc" style="left:66px;top:43px"><div class="ring"><svg viewBox="0 0 20 20" width="13" height="13"><rect x="2.5" y="5" width="12" height="8" fill="none" stroke="#2b2b2b" stroke-width="1.1"/><line x1="1" y1="14.5" x2="16" y2="14.5" stroke="#2b2b2b" stroke-width="1.1"/><rect x="12" y="8" width="5" height="4" fill="#fff" stroke="#2b2b2b" stroke-width="1"/><path d="M13 8V6.5a1.5 1.5 0 013 0V8" fill="none" stroke="#2b2b2b" stroke-width="1"/></svg></div><h5>PENETRATION TESTING</h5><p>Real attack methods used to probe your setup.</p><div class="go"></div></div>
  <div class="svc" style="left:105px;top:43px"><div class="ring"><svg viewBox="0 0 20 20" width="13" height="13"><circle cx="8.5" cy="8.5" r="5.5" fill="none" stroke="#2b2b2b" stroke-width="1.2"/><line x1="12.5" y1="12.5" x2="17" y2="17" stroke="#2b2b2b" stroke-width="1.6"/><path d="M7 6.5L5 8.5l2 2M10 6.5l2 2-2 2" fill="none" stroke="#2b2b2b" stroke-width=".9"/></svg></div><h5>CODE REVIEW</h5><p>Line by line checks of your source for flaws.</p><div class="go"></div></div>

  <div class="copy svc-copy1">
    <p>Each service can run on its own or as part of a wider program. We agree the scope with you first, test in line with your rules and share early warnings the moment we find something serious, so you never wait for the final report to act.</p>
    <p>Results come with clear steps to fix each issue and a free retest once your team is done.</p>
  </div>

  <div class="svc" style="left:28px;top:140px"><div class="ring"><svg viewBox="0 0 20 20" width="13" height="13"><circle cx="8.5" cy="8.5" r="5.5" fill="none" stroke="#2b2b2b" stroke-width="1.2"/><line x1="12.5" y1="12.5" x2="17" y2="17" stroke="#2b2b2b" stroke-width="1.6"/><circle cx="8.5" cy="8.5" r="2" fill="none" stroke="#2b2b2b" stroke-width=".9"/></svg></div><h5>BUG BOUNTY</h5><p>Crowd testing run by our own expert team.</p><div class="go"></div></div>
  <div class="svc" style="left:66px;top:140px"><div class="ring"><svg viewBox="0 0 20 20" width="13" height="13"><rect x="2.5" y="5" width="12" height="8" fill="none" stroke="#2b2b2b" stroke-width="1.1"/><line x1="1" y1="14.5" x2="16" y2="14.5" stroke="#2b2b2b" stroke-width="1.1"/><rect x="12" y="8" width="5" height="4" fill="#fff" stroke="#2b2b2b" stroke-width="1"/><path d="M13 8V6.5a1.5 1.5 0 013 0V8" fill="none" stroke="#2b2b2b" stroke-width="1"/></svg></div><h5>PENETRATION TESTING</h5><p>Real attack methods used to probe your setup.</p><div class="go"></div></div>
  <div class="svc" style="left:105px;top:140px"><div class="ring"><svg viewBox="0 0 20 20" width="13" height="13"><circle cx="8.5" cy="8.5" r="5.5" fill="none" stroke="#2b2b2b" stroke-width="1.2"/><line x1="12.5" y1="12.5" x2="17" y2="17" stroke="#2b2b2b" stroke-width="1.6"/><path d="M7 6.5L5 8.5l2 2M10 6.5l2 2-2 2" fill="none" stroke="#2b2b2b" stroke-width=".9"/></svg></div><h5>CODE REVIEW</h5><p>Line by line checks of your source for flaws.</p><div class="go"></div></div>

  <div class="svc" style="left:28px;top:196px"><div class="ring"><svg viewBox="0 0 20 20" width="13" height="13"><circle cx="8.5" cy="8.5" r="5.5" fill="none" stroke="#2b2b2b" stroke-width="1.2"/><line x1="12.5" y1="12.5" x2="17" y2="17" stroke="#2b2b2b" stroke-width="1.6"/><circle cx="8.5" cy="8.5" r="2" fill="none" stroke="#2b2b2b" stroke-width=".9"/></svg></div><h5>BUG BOUNTY</h5><p>Crowd testing run by our own expert team.</p><div class="go"></div></div>
  <div class="svc" style="left:66px;top:196px"><div class="ring"><svg viewBox="0 0 20 20" width="13" height="13"><rect x="2.5" y="5" width="12" height="8" fill="none" stroke="#2b2b2b" stroke-width="1.1"/><line x1="1" y1="14.5" x2="16" y2="14.5" stroke="#2b2b2b" stroke-width="1.1"/><rect x="12" y="8" width="5" height="4" fill="#fff" stroke="#2b2b2b" stroke-width="1"/><path d="M13 8V6.5a1.5 1.5 0 013 0V8" fill="none" stroke="#2b2b2b" stroke-width="1"/></svg></div><h5>PENETRATION TESTING</h5><p>Real attack methods used to probe your setup.</p><div class="go"></div></div>
  <div class="svc" style="left:105px;top:196px"><div class="ring"><svg viewBox="0 0 20 20" width="13" height="13"><circle cx="8.5" cy="8.5" r="5.5" fill="none" stroke="#2b2b2b" stroke-width="1.2"/><line x1="12.5" y1="12.5" x2="17" y2="17" stroke="#2b2b2b" stroke-width="1.6"/><path d="M7 6.5L5 8.5l2 2M10 6.5l2 2-2 2" fill="none" stroke="#2b2b2b" stroke-width=".9"/></svg></div><h5>CODE REVIEW</h5><p>Line by line checks of your source for flaws.</p><div class="go"></div></div>

  <div class="copy svc-copy2">
    <p>Each service can run on its own or as part of a wider program. We agree the scope with you first, test in line with your rules and share early warnings the moment we find something serious, so you never wait for the final report to act.</p>
    <p>Results come with clear steps to fix each issue and a free retest once your team is done.</p>
  </div>
  <footer class="site-footer">
    <div class="brand"><span class="brand-mark" style="border-color:#fff"></span><span class="brand-name">Emberstrat</span></div>
    <p class="foot-about">Security testing for firms of all sizes, run by certified local experts who care.</p>
    <div class="foot-col c1"><h4>SERVICES</h4>Bug bounty<br>Pen testing<br>Code review<br>Cloud audit<br>Red team<br>Training<br>Advice</div>
    <div class="foot-col c2"><h4>USEFUL LINK</h4>About us<br>Case studies<br>Blog<br>News<br>Careers<br>Privacy<br>Terms</div>
    <div class="foot-col c3"><h4>CONTACTS</h4>(02) 5550 1140<br>(02) 5550 1141<br>hello@emberstrat.com.au<br><h4>FOLLOW US</h4><div class="dots"><i></i><i></i><i></i><i></i><i></i></div></div>
    <p class="copyright">copyright © 2023 Emberstrat</p>
  </footer>
</div>

<!-- CASE STUDIES -->
<div class="page" style="left:611px">
  <div class="topbar"><div class="socials"><i></i><i></i><i></i><i></i><i></i></div><span class="tel">+61 2 5550 1140 &nbsp; +61 2 5550 1141</span><b class="call">CALL NOW</b></div>
  <header class="site-header"><div class="brand"><span class="brand-mark"></span><span class="brand-name">Emberstrat</span></div>
    <nav class="nav"><span>HOME</span><span>ABOUT</span><span>SERVICES</span><span class="on">CASE STUDIES</span><span>BLOG</span><span>NEWS</span><span>CONTACT US</span></nav></header>
  <h1 class="page-title about-title">CASE <em>STUDIES</em></h1>
  <section class="case-block">
    <div class="case-grid">
      <div style="background:#e9782f"><svg viewBox="0 0 20 20"><circle cx="10" cy="7" r="3.5" fill="none" stroke="#fff" stroke-width="1.1"/><path d="M3.5 17c0-4 3-6 6.5-6s6.5 2 6.5 6" fill="none" stroke="#fff" stroke-width="1.1"/></svg></div>
      <div style="background:#f0a044"><svg viewBox="0 0 20 20"><circle cx="10" cy="7" r="3.5" fill="none" stroke="#fff" stroke-width="1.1"/><path d="M3.5 17c0-4 3-6 6.5-6s6.5 2 6.5 6" fill="none" stroke="#fff" stroke-width="1.1"/></svg></div>
      <div style="background:#f6c58c"><svg viewBox="0 0 20 20"><circle cx="10" cy="7" r="3.5" fill="none" stroke="#ec6a3d" stroke-width="1.1"/><path d="M3.5 17c0-4 3-6 6.5-6s6.5 2 6.5 6" fill="none" stroke="#ec6a3d" stroke-width="1.1"/></svg></div>
      <div style="background:#fbe3c7"><svg viewBox="0 0 20 20"><circle cx="10" cy="7" r="3.5" fill="none" stroke="#ec6a3d" stroke-width="1.1"/><path d="M3.5 17c0-4 3-6 6.5-6s6.5 2 6.5 6" fill="none" stroke="#ec6a3d" stroke-width="1.1"/></svg></div>
      <div style="background:#fdf3ea"><svg viewBox="0 0 20 20"><circle cx="10" cy="7" r="3.5" fill="none" stroke="#2b2b2b" stroke-width="1.1"/><path d="M3.5 17c0-4 3-6 6.5-6s6.5 2 6.5 6" fill="none" stroke="#2b2b2b" stroke-width="1.1"/></svg></div>
      <div style="background:#fbe3c7"><svg viewBox="0 0 20 20"><circle cx="8" cy="7" r="3" fill="none" stroke="#ec6a3d" stroke-width="1.1"/><circle cx="13" cy="7.5" r="2.5" fill="none" stroke="#ec6a3d" stroke-width="1"/><path d="M2.5 16.5c0-3.5 2.5-5.5 5.5-5.5s5.5 2 5.5 5.5M14 11c2 .3 3.5 2 3.5 5" fill="none" stroke="#ec6a3d" stroke-width="1.1"/></svg></div>
      <div style="background:#fce7d2"><svg viewBox="0 0 20 20"><circle cx="6" cy="8" r="2.3" fill="none" stroke="#ec6a3d" stroke-width="1"/><circle cx="10" cy="6.5" r="2.5" fill="none" stroke="#ec6a3d" stroke-width="1"/><circle cx="14" cy="8" r="2.3" fill="none" stroke="#ec6a3d" stroke-width="1"/><path d="M2 16c0-3 2-4.5 4-4.5M18 16c0-3-2-4.5-4-4.5M5.5 16.5c0-3.5 2-5.5 4.5-5.5s4.5 2 4.5 5.5" fill="none" stroke="#ec6a3d" stroke-width="1"/></svg></div>
      <div style="background:#4a4a4a"><svg viewBox="0 0 20 20"><circle cx="4.5" cy="8.5" r="1.8" fill="none" stroke="#fff" stroke-width=".9"/><circle cx="8" cy="7" r="2.1" fill="none" stroke="#fff" stroke-width=".9"/><circle cx="12" cy="7" r="2.1" fill="none" stroke="#fff" stroke-width=".9"/><circle cx="15.5" cy="8.5" r="1.8" fill="none" stroke="#fff" stroke-width=".9"/><path d="M1.5 15.5c0-2.5 1.3-3.8 3-3.8M18.5 15.5c0-2.5-1.3-3.8-3-3.8M4.5 16c0-3 1.6-5 3.5-5M15.5 16c0-3-1.6-5-3.5-5M6.5 16.5c0-3 1.5-4.5 3.5-4.5s3.5 1.5 3.5 4.5" fill="none" stroke="#fff" stroke-width=".9"/></svg></div>
      <div style="background:#f0a044"><svg viewBox="0 0 20 20"><circle cx="10" cy="7" r="3.5" fill="none" stroke="#fff" stroke-width="1.1"/><path d="M3.5 17c0-4 3-6 6.5-6s6.5 2 6.5 6z" fill="none" stroke="#fff" stroke-width="1.1"/></svg></div>
      <div style="background:#ef8f2d"><svg viewBox="0 0 20 20"><circle cx="10" cy="7" r="3.5" fill="none" stroke="#fff" stroke-width="1.1"/><path d="M3.5 17c0-4 3-6 6.5-6s6.5 2 6.5 6z" fill="none" stroke="#fff" stroke-width="1.1"/></svg></div>
    </div>
  </section>
  <div class="copy case-copy">
    <p>From regional councils to fast growing tech firms, our clients trust us to test the systems they rely on. Each case shows the problem we were asked to solve, how we tested, what we found and how the client closed the gaps with our guidance and support over time.</p>
    <p>Read how we cut risk, met audit needs and built lasting security habits for teams of every size.</p>
  </div>
  <section class="stats">
    <div class="stat" style="left:6px"><b>455</b><small>FOLLOWERS</small></div>
    <div class="stat" style="left:47px"><b>1991</b><small>SINCE</small></div>
    <div class="stat" style="left:89px"><b>806</b><small>HAPPY CLIENTS</small></div>
    <div class="stat" style="left:131px"><b>923</b><small>PROJECTS</small></div>
  </section>
  <footer class="site-footer">
    <div class="brand"><span class="brand-mark" style="border-color:#fff"></span><span class="brand-name">Emberstrat</span></div>
    <p class="foot-about">Security testing for firms of all sizes, run by certified local experts who care.</p>
    <div class="foot-col c1"><h4>SERVICES</h4>Bug bounty<br>Pen testing<br>Code review<br>Cloud audit<br>Red team<br>Training<br>Advice</div>
    <div class="foot-col c2"><h4>USEFUL LINK</h4>About us<br>Case studies<br>Blog<br>News<br>Careers<br>Privacy<br>Terms</div>
    <div class="foot-col c3"><h4>CONTACTS</h4>(02) 5550 1140<br>(02) 5550 1141<br>hello@emberstrat.com.au<br><h4>FOLLOW US</h4><div class="dots"><i></i><i></i><i></i><i></i><i></i></div></div>
    <p class="copyright">copyright © 2023 Emberstrat</p>
  </footer>
</div>

<!-- BLOG -->
<div class="page" style="left:802px">
  <div class="topbar"><div class="socials"><i></i><i></i><i></i><i></i><i></i></div><span class="tel">+61 2 5550 1140 &nbsp; +61 2 5550 1141</span><b class="call">CALL NOW</b></div>
  <header class="site-header"><div class="brand"><span class="brand-mark"></span><span class="brand-name">Emberstrat</span></div>
    <nav class="nav"><span>HOME</span><span>ABOUT</span><span>SERVICES</span><span>CASE STUDIES</span><span class="on">BLOG</span><span>NEWS</span><span>CONTACT US</span></nav></header>
  <h1 class="page-title about-title">BLOG</h1>
  <article class="blog-card on-dark" style="left:10px;top:46px;background:#ea6a3e"><h5>LOREM IPSUM DOL</h5><p>Lorem ipsum dolor sit amet, consectetue a commodo consequat. Duis aute</p><time>▦ 24 April 2023</time></article>
  <article class="blog-card on-dark" style="left:87px;top:46px;background:#ef9130"><h5>LOREM IPSUM DOL</h5><p>Lorem ipsum dolor sit amet, consectetue a commodo consequat. Duis aute</p><time>▦ 24 April 2023</time></article>
  <article class="blog-card on-light" style="left:10px;top:113px;background:#f6cb94"><h5>LOREM IPSUM DOL</h5><p>Lorem ipsum dolor sit amet, consectetue a commodo consequat. Duis aute</p><time>▦ 24 April 2023</time></article>
  <article class="blog-card on-dark" style="left:87px;top:113px;background:#f2a941"><h5>LOREM IPSUM DOL</h5><p>Lorem ipsum dolor sit amet, consectetue a commodo consequat. Duis aute</p><time>▦ 24 April 2023</time></article>
  <article class="blog-card on-light" style="left:10px;top:180px;background:#fbe6d2"><h5>LOREM IPSUM DOL</h5><p>Lorem ipsum dolor sit amet, consectetue a commodo consequat. Duis aute</p><time>▦ 24 April 2023</time></article>
  <article class="blog-card on-light" style="left:87px;top:180px;background:#fdf4ea"><h5>LOREM IPSUM DOL</h5><p>Lorem ipsum dolor sit amet, consectetue a commodo consequat. Duis aute</p><time>24 April 2023</time></article>
  <footer class="site-footer">
    <div class="brand"><span class="brand-mark" style="border-color:#fff"></span><span class="brand-name">Emberstrat</span></div>
    <p class="foot-about">Security testing for firms of all sizes, run by certified local experts who care.</p>
    <div class="foot-col c1"><h4>SERVICES</h4>Bug bounty<br>Pen testing<br>Code review<br>Cloud audit<br>Red team<br>Training<br>Advice</div>
    <div class="foot-col c2"><h4>USEFUL LINK</h4>About us<br>Case studies<br>Blog<br>News<br>Careers<br>Privacy<br>Terms</div>
    <div class="foot-col c3"><h4>CONTACTS</h4>(02) 5550 1140<br>(02) 5550 1141<br>hello@emberstrat.com.au<br><h4>FOLLOW US</h4><div class="dots"><i></i><i></i><i></i><i></i><i></i></div></div>
    <p class="copyright">copyright © 2023 Emberstrat</p>
  </footer>
</div>

<!-- CONTACT -->
<div class="page" style="left:993px">
  <div class="topbar"><div class="socials"><i></i><i></i><i></i><i></i><i></i></div><span class="tel">+61 2 5550 1140 &nbsp; +61 2 5550 1141</span><b class="call">CALL NOW</b></div>
  <header class="site-header"><div class="brand"><span class="brand-mark"></span><span class="brand-name">Emberstrat</span></div>
    <nav class="nav"><span>HOME</span><span>ABOUT</span><span>SERVICES</span><span>CASE STUDIES</span><span>BLOG</span><span>NEWS</span><span class="on">CONTACT US</span></nav></header>
  <h1 class="page-title about-title">CONTACT <em>US</em></h1>
  <section class="contact-form">
    <div class="field" style="top:6.5px;height:11.5px">Name:</div>
    <div class="field" style="top:20.5px;height:11.5px">Email Adress:</div>
    <div class="field" style="top:35px;height:11.5px">Subject:</div>
    <div class="field" style="top:49.5px;height:49.5px">Your Message:</div>
    <span class="btn">SEND MESSAGE</span>
  </section>
  <div class="contact-lines">
    <div><svg viewBox="0 0 10 10"><path d="M5 9.5S1.5 5.8 1.5 3.8a3.5 3.5 0 017 0C8.5 5.8 5 9.5 5 9.5z" fill="var(--orange)"/></svg>12 Harbour Lane, Sydney NSW 2000, Australia, open Monday to Friday</div>
    <div><span><svg viewBox="0 0 10 10"><path d="M2 1l2 2-1 1.5c.8 1.5 1.5 2.2 3 3L7.5 6.5l2 2L8 10C4 9.5.5 6 0 2z" fill="var(--orange)"/></svg>(02) 5550 1140</span><span><svg viewBox="0 0 10 10"><path d="M2 1l2 2-1 1.5c.8 1.5 1.5 2.2 3 3L7.5 6.5l2 2L8 10C4 9.5.5 6 0 2z" fill="var(--orange)"/></svg>(02) 5550 1141</span><span><svg viewBox="0 0 10 10"><rect x=".5" y="2" width="9" height="6" fill="var(--orange)"/></svg>hello@emberstrat.com.au</span></div>
  </div>
  <section class="map" role="img" aria-label="World map with office location pins"></section>
  <section class="follow"><h3>FOLLOW <em>US</em></h3><div class="dots"><i></i><i></i><i></i><i></i><i></i></div></section>
  <footer class="site-footer">
    <div class="brand"><span class="brand-mark" style="border-color:#fff"></span><span class="brand-name">Emberstrat</span></div>
    <p class="foot-about">Security testing for firms of all sizes, run by certified local experts who care.</p>
    <div class="foot-col c1"><h4>SERVICES</h4>Bug bounty<br>Pen testing<br>Code review<br>Cloud audit<br>Red team<br>Training<br>Advice</div>
    <div class="foot-col c2"><h4>USEFUL LINK</h4>About us<br>Case studies<br>Blog<br>News<br>Careers<br>Privacy<br>Terms</div>
    <div class="foot-col c3"><h4>CONTACTS</h4>(02) 5550 1140<br>(02) 5550 1141<br>hello@emberstrat.com.au<br><h4>FOLLOW US</h4><div class="dots"><i></i><i></i><i></i><i></i><i></i></div></div>
    <p class="copyright">copyright © 2023 Emberstrat</p>
  </footer>
</div>

</div>
</body>
</html>
```